BLUE HAVEN (Business Card for Training Company)

Blue Haven is a training and consultancy company with a focus on executive protection and medical. I would like the card to be nice and sharp, not overdone and in black and red. I would also like it to highlight that it is "A Dravin Company"

I would like it to be simple and highlight a few things.

1. Name
2. Title
3. Phone Number
4. Email

I would also like www.dravinholdings.example/blue-haven to be on the card somewhere.

Target Market(s)

Security Companies

Industry/Entity Type

Security

Contact Information for Business Card

Blue Haven is a training and consultancy company with a focus on executive protection and medical. I would like the card to be nice and sharp, not overdone and in black and red. I would also like it to highlight that it is "A Dravin Company" I would like it to be simple and highlight a few things. 1. Name 2. Title 3. Phone Number 4. Email I would also like www.dravinholdings.example/blue-haven to be on the card somewhere.

Requirements
Must have
• A Dravin Company listed on the card and the website
Nice to have
• Highlight Medical Training, Consultancy & Executive Protection Courses

```html
<!DOCTYPE html>
<html lang="en">
<head>
<meta charset="utf-8">
<title>Blue Haven — Business Card</title>
<link rel="stylesheet" href="https://fonts.googleapis.com/css2?family=Montserrat:wght@700;800;900&family=Michroma&family=Poppins:wght@400;500&display=swap">
<style>
  :root {
    --stage: #2b2b2d;
    --ink: #0c0c0c;
    --paper: #ffffff;
    --red: #8e1a1c;
    --red-light: #a3282b;
    --rule: #8a8a8a;
    --white: #ffffff;
  }
  * { box-sizing: border-box; margin: 0; padding: 0; }
  html, body { width: 1200px; height: 900px; overflow: hidden; }
  body {
    background: var(--stage);
    display: flex;
    flex-direction: column;
    align-items: center;
    justify-content: center;
    gap: 56px;
  }
  .card {
    position: relative;
    width: 640px;
    height: 366px;
    border-radius: 22px;
    overflow: hidden;
  }

  /* Back side */
  .card--back { background: var(--ink); }
  .card--back .wordmark {
    position: absolute;
    left: 0; right: 0; top: 92px;
    text-align: center;
    font-family: "Montserrat", sans-serif;
    font-weight: 900;
    font-size: 62px;
    line-height: 0.92;
    letter-spacing: 1px;
    color: var(--white);
  }
  .card--back .web {
    position: absolute;
    left: 0; right: 0; bottom: 58px;
    text-align: center;
    font-family: "Michroma", sans-serif;
    font-size: 12px;
    letter-spacing: 1px;
    color: var(--white);
    white-space: nowrap;
  }
  .card--back .web span { color: var(--red-light); }

  /* Front side */
  .card--front { background: var(--paper); }
  .card--front .band { position: absolute; inset: 0; width: 100%; height: 100%; }
  .brand-block {
    position: absolute;
    left: 34px; top: 104px;
  }
  .card--front .wordmark {
    font-family: "Montserrat", sans-serif;
    font-weight: 900;
    font-size: 54px;
    line-height: 0.92;
    color: var(--ink);
  }
  .parent-line {
    margin-top: 8px;
    font-family: "Montserrat", sans-serif;
    font-weight: 800;
    font-size: 11px;
    letter-spacing: 1.5px;
    color: var(--red);
    white-space: nowrap;
  }
  .divider {
    position: absolute;
    left: 290px; top: 56px;
    width: 1.5px; height: 136px;
    background: var(--rule);
  }
  .contact-block {
    position: absolute;
    left: 308px; top: 52px;
  }
  .person-name {
    font-family: "Montserrat", sans-serif;
    font-weight: 900;
    font-size: 24px;
    letter-spacing: 0.5px;
    color: var(--ink);
    white-space: nowrap;
  }
  .person-title {
    font-family: "Montserrat", sans-serif;
    font-weight: 800;
    font-size: 12.5px;
    letter-spacing: 1px;
    color: var(--red);
    margin-top: 2px;
    margin-bottom: 12px;
    white-space: nowrap;
  }
  .contact-list { list-style: none; }
  .contact-list li {
    display: flex;
    align-items: center;
    gap: 9px;
    font-family: "Poppins", sans-serif;
    font-size: 13px;
    color: var(--ink);
    margin-bottom: 7px;
    white-space: nowrap;
  }
  .contact-list .accent { color: var(--red); }
  .contact-icon { width: 20px; height: 22px; flex: none; }
</style>
</head>
<body>

  <section class="card card--back" aria-label="Card back">
    <div class="wordmark">BLUE<br>HAVEN</div>
    <p class="web">WWW.DRAVINHOLDINGS.EXAMPLE/<span>BLUE-HAVEN</span></p>
  </section>

  <section class="card card--front" aria-label="Card front">
    <svg class="band" viewBox="0 0 640 366" preserveAspectRatio="none" aria-hidden="true">
      <defs>
        <linearGradient id="band-sheen" x1="0" y1="1" x2="1" y2="0">
          <stop offset="0" stop-color="#8e1a1c"/>
          <stop offset="1" stop-color="#a8302f"/>
        </linearGradient>
      </defs>
      <polygon points="0,300 470,262 640,200 640,366 0,366" fill="url(#band-sheen)"/>
    </svg>

    <div class="brand-block">
      <div class="wordmark">BLUE<br>HAVEN</div>
      <p class="parent-line">A DRAVIN COMPANY</p>
    </div>
    <div class="divider"></div>

    <div class="contact-block">
      <h1 class="person-name">MARTIN HALE</h1>
      <p class="person-title">MANAGING DIRECTOR</p>
      <ul class="contact-list">
        <li>
          <svg class="contact-icon" viewBox="0 0 20 22" aria-hidden="true">
            <path d="M2 2h16v12l-8 6-8-6z" fill="var(--red)"/>
            <path d="M7 6c0 4 3 7 6 7l1-2-2-1-1 1c-1-.5-2-1.5-2.5-2.5l1-1-1-2z" fill="#fff"/>
          </svg>
          555-014-2290
        </li>
        <li>
          <svg class="contact-icon" viewBox="0 0 20 22" aria-hidden="true">
            <path d="M2 2h16v12l-8 6-8-6z" fill="var(--red)"/>
            <rect x="5" y="6" width="10" height="7" fill="none" stroke="#fff" stroke-width="1.2"/>
            <path d="M5 6l5 4 5-4" fill="none" stroke="#fff" stroke-width="1.2"/>
          </svg>
          info@dravinholdings.example
        </li>
        <li>
          <svg class="contact-icon" viewBox="0 0 20 22" aria-hidden="true">
            <path d="M2 2h16v12l-8 6-8-6z" fill="var(--red)"/>
            <circle cx="10" cy="9.5" r="4.5" fill="none" stroke="#fff" stroke-width="1.1"/>
            <path d="M5.5 9.5h9M10 5v9M7.5 6.5c1.5 2 1.5 4 0 6M12.5 6.5c-1.5 2-1.5 4 0 6" fill="none" stroke="#fff" stroke-width="0.9"/>
          </svg>
          <span>www.dravinholdings.example/<span class="accent">blue-haven</span></span>
        </li>
      </ul>
    </div>
  </section>

</body>
</html>
```